PCとスマホデザインの両方納品をいただきますが、
まずはデザインイメージが確認しやすいPCページのみの提案をお願いします。
スマホページは当選者に納品時にお願いしたいと思います。
スマホサイズについて、カンバスサイズは横幅375pxで作成し、2倍の横幅750pxのサイズで書き出ししてください。
(Clarexディスプレイに対応するため)
スマホページ作成時は、メニューが展開した際のデザインもお願いします。
レスポンシブウェブデザインを意識したデザインでお願いします。

```html
<!DOCTYPE html>
<html lang="ja">
<head>
<meta charset="utf-8">
<title>蒼進 SOSHIN</title>
<link href="https://fonts.googleapis.com/css2?family=Noto+Sans+JP:wght@400;500;700;900&family=Oswald:wght@400;600&display=swap" rel="stylesheet">
<style>
:root{
  --navy:#173a78;
  --blue:#1f5fbf;
  --sky:#3a8fd8;
  --ink:#222;
  --muted:#666;
  --line:#d9dde3;
  --pale:#f2f3f5;
  --white:#fff;
  --photo-grey:#9aa0a6;
  --photo-dark:#4b5158;
}
*{box-sizing:border-box;margin:0;padding:0}
html,body{width:1200px;height:5200px;overflow:hidden}
body{font-family:"Noto Sans JP",sans-serif;color:var(--ink);background:var(--white);font-size:14px;line-height:1.8}
.photo{display:block;background:linear-gradient(135deg,var(--photo-grey),var(--photo-dark))}
.en{font-family:"Oswald",sans-serif;letter-spacing:.15em;color:var(--blue);font-size:13px}
.brand{font-family:"Noto Sans JP",sans-serif;font-weight:900;color:var(--navy);letter-spacing:.04em}

/* header */
.site-header{height:64px;display:flex;align-items:center;padding:0 0 0 28px;position:relative}
.site-header .tagline{position:absolute;top:4px;left:28px;font-size:10px;color:var(--muted)}
.site-header .brand{font-size:26px;margin-top:10px}
.global-nav{margin-left:auto;display:flex;gap:34px;font-size:12px;font-weight:500;margin-right:30px}
.header-cta{background:var(--navy);color:var(--white);height:64px;width:150px;display:flex;align-items:center;justify-content:center;font-size:12px;gap:8px}

/* hero */
.hero{height:640px;position:relative;background:linear-gradient(180deg,#c7ccd2,#e9ecef 60%,#cfd4d9)}
.hero .person-left{position:absolute;left:0;top:0;width:380px;height:640px;background:linear-gradient(160deg,#555b62,#23272c)}
.hero .person-right{position:absolute;right:0;top:0;width:400px;height:640px;background:linear-gradient(200deg,#5d636a,#202428)}
.hero-copy{position:absolute;left:0;right:0;top:110px;text-align:center}
.hero-copy h1{font-size:44px;font-weight:900;color:var(--blue);font-style:italic;line-height:1.35;text-shadow:0 2px 0 #fff}
.hero-copy .brand{font-size:110px;line-height:1.1;margin-top:30px}
.hero-copy .brand-en{font-family:"Oswald",sans-serif;color:var(--navy);letter-spacing:.4em;font-size:18px}
.hero-values{display:flex;justify-content:center;gap:14px;margin-top:40px}
.hero-values span{background:var(--navy);color:var(--white);font-weight:900;font-size:36px;padding:4px 24px;font-style:italic}

/* section heads */
.section-head{text-align:center;padding-top:64px}
.section-head h2{font-size:30px;font-weight:700;letter-spacing:.12em;line-height:1.4}
.section-head .en{display:block;margin-top:4px}

/* service */
.service{height:1750px;position:relative}
.svc-a-photo{position:absolute;left:0;top:200px;width:760px;height:380px}
.svc-a-text{position:absolute;left:700px;top:220px;width:460px;background:var(--white);padding:30px 34px;box-shadow:0 2px 10px rgba(0,0,0,.08)}
.svc-title{font-size:20px;font-weight:700;color:var(--navy);border-left:5px solid var(--blue);padding-left:12px;line-height:1.4;margin-bottom:16px}
.svc-text{font-size:13px;color:var(--muted);line-height:2}
.partner{display:flex;align-items:center;justify-content:flex-end;gap:12px;margin-top:18px;font-size:11px;color:var(--muted)}
.partner .badge{width:86px;height:26px;background:var(--navy);border-radius:3px}
.svc-a-sub1{position:absolute;left:40px;top:600px;width:330px;height:260px}
.svc-a-sub2{position:absolute;left:390px;top:600px;width:330px;height:260px}
.svc-a-sub3{position:absolute;left:740px;top:620px;width:420px;height:240px}

.svc-b-text{position:absolute;left:40px;top:970px;width:560px}
.svc-b-photo{position:absolute;left:640px;top:930px;width:560px;height:540px;background:linear-gradient(160deg,#6f7478,#2f3337)}
.svc-b-sub{position:absolute;left:640px;top:1490px;width:300px;height:180px;background:linear-gradient(135deg,#7b8a5e,#44503a)}
.svc-b-sub2{position:absolute;left:960px;top:1490px;width:240px;height:180px}
.sub-title{font-size:17px;font-weight:700;color:var(--blue);margin:28px 0 10px;border-bottom:2px solid var(--blue);display:inline-block;padding-bottom:2px}
.spec-table{border-collapse:collapse;width:480px;margin:26px auto 0;font-size:12px}
.spec-table caption{background:var(--navy);color:var(--white);font-weight:700;padding:6px;font-size:13px}
.spec-table th{background:#dfe7f3;color:var(--navy);padding:6px;border:1px solid var(--line);font-weight:500}
.spec-table td{padding:10px 12px;border:1px solid var(--line);vertical-align:top;color:var(--muted);line-height:1.9}

/* origin */
.origin{height:640px;background:var(--pale);position:relative}
.origin-head{position:absolute;left:560px;top:70px;text-align:center;width:300px}
.origin-head h2{font-size:30px;font-weight:700;letter-spacing:.12em;line-height:1.4}
.origin-head .brand{position:absolute;left:360px;top:-10px;font-size:62px;line-height:1;white-space:nowrap}
.origin-head .brand small{display:block;font-family:"Oswald",sans-serif;font-size:14px;letter-spacing:.4em;margin-top:6px}
.origin-text{position:absolute;left:40px;top:230px;width:600px;font-size:13px;line-height:2.2;color:var(--ink)}
.origin-photo{position:absolute;left:700px;top:220px;width:460px;height:360px;background:linear-gradient(160deg,#8fa6b4,#3e4a3c)}

/* company */
.company{height:1260px;position:relative}
.company-table{position:absolute;left:100px;top:200px;width:1000px;border-collapse:collapse;font-size:13px}
.company-table th{width:200px;background:var(--pale);text-align:left;padding:18px 24px;border-bottom:1px solid var(--line);font-weight:500;vertical-align:top}
.company-table td{padding:18px 24px;border-bottom:1px solid var(--line);line-height:2}
.company-map{position:absolute;left:300px;top:830px;width:800px;height:380px;background:linear-gradient(135deg,#e8ecef,#d7dde2)}
.map-pin{position:absolute;left:560px;top:130px}

/* contact */
.contact{height:440px;position:relative;background:linear-gradient(180deg,#dbe3ea,#eef1f4)}
.contact .person-left{position:absolute;left:0;bottom:0;width:320px;height:440px;background:linear-gradient(160deg,#555b62,#23272c)}
.contact .person-right{position:absolute;right:0;bottom:0;width:320px;height:440px;background:linear-gradient(200deg,#5d636a,#202428)}
.contact-box{position:absolute;left:330px;right:330px;top:80px;text-align:center}
.contact-box h2{font-size:30px;font-weight:700;color:var(--navy);letter-spacing:.1em;line-height:1.4}
.contact-box p{font-size:12px;color:var(--muted);margin-top:18px}
.contact-btn{display:inline-flex;align-items:center;gap:10px;background:var(--navy);color:var(--white);padding:14px 46px;margin-top:28px;font-size:14px}

/* footer */
.site-footer{background:var(--pale);height:446px;text-align:center;padding-top:40px}
.footer-nav{display:flex;justify-content:center;gap:40px;font-size:12px}
.site-footer .tagline{font-size:10px;color:var(--muted);margin-top:46px}
.site-footer .brand{font-size:46px;line-height:1.2}
.site-footer .brand-en{font-family:"Oswald",sans-serif;color:var(--navy);letter-spacing:.4em;font-size:12px}
.site-footer address{font-style:normal;font-size:11px;color:var(--muted);margin-top:20px}
.copyright{font-size:10px;color:var(--muted);margin-top:40px}
</style>
</head>
<body>

<header class="site-header">
  <p class="tagline">耐火被覆・OAフロア工事の専門会社</p>
  <div class="brand">蒼進</div>
  <nav class="global-nav">
    <span>TOP</span><span>耐火被覆工事</span><span>フリーアクセスフロア</span><span>会社名由来</span><span>会社概要</span>
  </nav>
  <a class="header-cta">
    <svg width="16" height="12" viewBox="0 0 16 12"><rect x="0.5" y="0.5" width="15" height="11" fill="none" stroke="#fff"/><path d="M1 1l7 6 7-6" fill="none" stroke="#fff"/></svg>
    お問い合わせ
  </a>
</header>

<section class="hero">
  <div class="person-left" role="img" aria-label="腕を組む作業服姿の職人の写真"></div>
  <div class="person-right" role="img" aria-label="腕を組む作業服姿の職人の写真"></div>
  <div class="hero-copy">
    <h1>新生・再生し続ける、<br>都市と建物と共に。</h1>
    <div class="brand">蒼進</div>
    <div class="brand-en">SOSHIN</div>
    <div class="hero-values"><span>力</span><span>希望</span><span>確信</span></div>
  </div>
</section>

<section class="service">
  <div class="section-head"><h2>事業内容</h2><span class="en">SERVICE</span></div>

  <div class="svc-a-photo photo" role="img" aria-label="鉄骨天井に耐火被覆を施工した現場の写真"></div>
  <div class="svc-a-text">
    <h3 class="svc-title">耐火被覆工事（巻付け）</h3>
    <p class="svc-text">建物の骨組みを火災の熱から守るため、鉄骨の柱や梁に耐火材を巻き付ける工事です。認定工法に基づき、一つひとつの部材を丁寧に施工し、建物と人の安全を支えています。高所作業車を用いた大規模な現場にも対応いたします。</p>
    <div class="partner"><span>巻付け工法 認定施工店</span><span class="badge"></span></div>
  </div>
  <div class="svc-a-sub1 photo" role="img" aria-label="高所作業車の上で施工する職人の写真"></div>
  <div class="svc-a-sub2 photo" role="img" aria-label="柱に耐火材を巻き付ける職人の写真"></div>
  <div class="svc-a-sub3 photo" role="img" aria-label="耐火被覆を終えた鉄骨の写真"></div>

  <div class="svc-b-text">
    <h3 class="svc-title">フリーアクセスフロア（OAフロア工事）</h3>
    <p class="svc-text">フリーアクセスフロアは、床下に配線スペースを設ける二重床の工事です。オフィスやサーバールームなどで、LAN や電源の配線を床下にすっきり納め、レイアウト変更にも柔軟に対応できる快適な空間をつくります。</p>
    <p class="svc-text">新築はもちろん、既存オフィスの改修工事にも対応しております。</p>
    <h4 class="sub-title">木工事</h4>
    <p class="svc-text">床の下地づくりや造作など、木工事も自社で対応しています。OAフロアと合わせてご依頼いただくことで、工期の短縮にもつながります。</p>
    <table class="spec-table">
      <caption>取扱メーカー</caption>
      <tr><th>OAフロア</th><th>木床</th><th>その他</th></tr>
      <tr>
        <td>ノルテ工業株式会社<br>株式会社アスカ<br>三和床材株式会社<br>サクラフロア株式会社</td>
        <td>二重床<br>束床<br>乾式遮音<br>置床</td>
        <td>下地材<br>巾木・見切<br>タイルカーペット</td>
      </tr>
    </table>
  </div>
  <div class="svc-b-photo" role="img" aria-label="パネルを敷き込み中のOAフロア床の写真"></div>
  <div class="svc-b-sub" role="img" aria-label="OAフロアパネルの拡大写真"></div>
  <div class="svc-b-sub2 photo" role="img" aria-label="施工完了後の床の写真"></div>
</section>

<section class="origin">
  <div class="origin-head">
    <h2>会社名由来</h2><span class="en">ORIGIN</span>
    <div class="brand">蒼進<small>SOSHIN</small></div>
  </div>
  <p class="origin-text">社名の「蒼進（そうしん）」には、澄んだ空のように真っ直ぐな心で、常に前へ進み続けたいという想いを込めています。創業以来、一つひとつの現場に誠実に向き合い、職人の技術と信頼を積み重ねてまいりました。<br><br>「力」「希望」「確信」を胸に、建物の新生と再生に携わり、これからも都市とともに歩み続けてまいります。お客様、協力会社、そして社員一人ひとりと手を取り合い、次の世代へ確かな仕事をつないでいくことが私たちの使命です。</p>
  <div class="origin-photo" role="img" aria-label="青空の下に立つ武将の銅像の写真"></div>
</section>

<section class="company">
  <div class="section-head"><h2>会社概要</h2><span class="en">COMPANY</span></div>
  <table class="company-table">
    <tr><th>会社名</th><td>有限会社蒼進</td></tr>
    <tr><th>本社</th><td>〒000-0000　東京都架空区みなと町1丁目2番3号 みなとビル2階</td></tr>
    <tr><th>設立</th><td>平成17年（2005年）3月</td></tr>
    <tr><th>代表</th><td>代表取締役　青山 進一</td></tr>
    <tr><th>事業内容</th><td>耐火被覆工事（巻付け）・フリーアクセスフロア（OAフロア）・木工工事</td></tr>
    <tr><th>主な取引先（順不同）</th><td>株式会社ノルテ<br>港建設株式会社<br>ミナト工業株式会社<br>株式会社アスカ建装<br>株式会社サクラ<br>東和興業株式会社<br>株式会社青葉</td></tr>
    <tr><th>建設業許可</th><td>東京都知事許可（般-00）第00000号<br>内装仕上工事業<br>とび・土工工事業</td></tr>
    <tr><th>アクセス</th><td></td></tr>
  </table>
  <div class="company-map" role="img" aria-label="本社周辺の地図">
    <svg class="map-pin" width="28" height="40" viewBox="0 0 28 40"><path d="M14 0C6 0 0 6 0 14c0 10 14 26 14 26s14-16 14-26C28 6 22 0 14 0z" fill="#d93025"/><circle cx="14" cy="14" r="5" fill="#fff"/></svg>
  </div>
</section>

<section class="contact">
  <div class="person-left" role="img" aria-label="作業服姿の職人の写真"></div>
  <div class="person-right" role="img" aria-label="作業服姿の職人の写真"></div>
  <div class="contact-box">
    <h2>お問い合わせ・社員募集</h2>
    <span class="en">CONTACT / RECRUIT</span>
    <p>工事のご相談やお見積り、求人へのご応募はお問い合わせフォームよりお気軽にご連絡ください。</p>
    <a class="contact-btn">
      <svg width="16" height="12" viewBox="0 0 16 12"><rect x="0.5" y="0.5" width="15" height="11" fill="none" stroke="#fff"/><path d="M1 1l7 6 7-6" fill="none" stroke="#fff"/></svg>
      お問い合わせフォームはこちら
    </a>
  </div>
</section>

<footer class="site-footer">
  <nav class="footer-nav">
    <span>TOP</span><span>耐火被覆工事</span><span>フリーアクセスフロア</span><span>会社名由来</span><span>会社概要</span><span>お問い合わせ</span>
  </nav>
  <p class="tagline">耐火被覆・OAフロア工事の専門会社</p>
  <div class="brand">蒼進</div>
  <div class="brand-en">SOSHIN</div>
  <address>〒000-0000　東京都架空区みなと町1丁目2番3号 みなとビル2階　TEL 00-0000-0000</address>
  <p class="copyright">© SOSHIN</p>
</footer>

</body>
</html>
```